Harbor Oak Works business cards

I’d like a business card design that includes my logo, a tag line and my contact info. Black, textured background. My contact info color should match the orange and blue gradients. Tagline under logo: “Wooden Tables and Furniture of the Highest Quality”

Target Market(s)

High end furniture buyers

Contact Information for Business Card

Contact info, logo and tagline

```html
<!DOCTYPE html>
<html lang="en">
<head>
<meta charset="utf-8">
<title>Harbor Oak Works – Business Cards</title>
<link rel="stylesheet" href="https://fonts.googleapis.com/css2?family=Open+Sans:wght@400;600&family=Roboto+Condensed:wght@400&display=swap">
<style>
  :root {
    --backdrop: #3a332f;
    --card: #252525;
    --orange: #f0702a;
    --orange-light: #f59a4a;
    --blue: #3f86e0;
    --text: #e8e8e8;
    --rule: #8a8a8a;
  }
  * { margin: 0; padding: 0; box-sizing: border-box; }
  html, body {
    width: 1200px; height: 716px; overflow: hidden;
    background: var(--backdrop);
  }
  .canvas {
    position: relative; width: 1200px; height: 716px;
    display: flex; align-items: center; justify-content: center; gap: 24px;
  }
  .card {
    position: relative; width: 560px; height: 320px;
    background: var(--card); overflow: hidden;
    box-shadow: 0 10px 28px rgba(0,0,0,0.45);
    font-family: "Open Sans", sans-serif; color: var(--text);
  }
  .brand { position: absolute; }
  .brand-name {
    display: flex; align-items: center; gap: 8px;
    font-family: "Open Sans", sans-serif; font-weight: 600;
    color: var(--orange); white-space: nowrap;
  }
  .brand-dot { border-radius: 50%; background: var(--orange); flex: none; }
  .brand-tagline {
    font-family: "Roboto Condensed", sans-serif; color: var(--blue);
    white-space: nowrap;
  }
  .card-front .brand { left: 30px; top: 26px; }
  .card-front .brand-name { font-size: 26px; }
  .card-front .brand-dot { width: 12px; height: 12px; }
  .card-front .brand-tagline { font-size: 11px; margin-top: 2px; }

  .person { position: absolute; left: 30px; top: 112px; }
  .person-name { font-size: 22px; color: var(--orange); line-height: 1.1; }
  .person-title { font-size: 12px; margin-top: 2px; }
  .divider {
    position: absolute; left: 30px; top: 172px; width: 290px;
    height: 1px; background: var(--rule);
  }
  .contact-list { position: absolute; left: 30px; top: 186px; list-style: none; font-size: 12px; line-height: 20px; }
  .contact-list li { display: flex; align-items: center; gap: 8px; }
  .contact-list svg { width: 11px; height: 11px; fill: var(--orange); flex: none; }
  .address { position: absolute; left: 190px; top: 226px; font-size: 12px; line-height: 18px; font-style: normal; }
  .address .web { color: var(--orange); }

  .tree-art {
    position: absolute;
    background: radial-gradient(ellipse at 50% 40%, rgba(245,140,60,0.75) 0%, rgba(240,112,42,0.45) 45%, rgba(37,37,37,0) 72%);
  }
  .card-front .tree-art { right: 0; top: 0; width: 220px; height: 320px; }
  .card-back .tree-art { left: 0; top: 0; width: 300px; height: 320px; }

  .card-back .brand { right: 32px; bottom: 40px; text-align: right; }
  .card-back .brand-name { font-size: 34px; justify-content: flex-end; }
  .card-back .brand-dot { width: 14px; height: 14px; }
  .card-back .brand-tagline { font-size: 14px; margin-top: 4px; }
</style>
</head>
<body>
<main class="canvas">
  <section class="card card-front">
    <div class="brand">
      <div class="brand-name"><span class="brand-dot"></span>Harbor Oak Works</div>
      <div class="brand-tagline">Wooden Tables &amp; Furniture of the Highest Quality</div>
    </div>
    <div class="person">
      <div class="person-name">Daniel Whitmore</div>
      <div class="person-title">Managing Director</div>
    </div>
    <div class="divider"></div>
    <ul class="contact-list">
      <li><svg viewBox="0 0 12 12"><path d="M3 1l2 2-1 1.5c.6 1.4 1.6 2.4 3 3L8.5 6.5l2 2L9.5 10.5C5 10 2 7 1.5 2.5z"/></svg>555-213-4870</li>
      <li><svg viewBox="0 0 12 12"><path d="M3 0h6v12H3zM4 1.5v8h4v-8z"/></svg>555-309-6142</li>
      <li><svg viewBox="0 0 12 12"><path d="M0 2h12v8H0zM1 3l5 4 5-4z"/></svg>info@HarborOakWorks</li>
    </ul>
    <address class="address">
      412 Alder Ridge Road<br>
      Juneau, Alaska 99801<br>
      <span class="web">www.HarborOakWorks.com</span>
    </address>
    <div class="tree-art" role="img" aria-label="Orange bare-branched tree illustration"></div>
  </section>

  <section class="card card-back">
    <div class="tree-art" role="img" aria-label="Orange bare-branched tree illustration"></div>
    <div class="brand">
      <div class="brand-name"><span class="brand-dot"></span>Harbor Oak Works</div>
      <div class="brand-tagline">Wooden Tables &amp; Furniture of the Highest Quality</div>
    </div>
  </section>
</main>
</body>
</html>
```